Plaxo - Booking activities for Kids and Adults.

The app allows booking of Kid's activities for a given date/time.
The app lists activities offered via various clubs (vendors) which a user can book for their kids.
The users can browse various clubs and their offered activities. The users can manage their kid's profiles.
Need a whole new look to the app. The existing app can be checked out at
https://store.example-apps.test/details?id=com.plaxokw
https://apps.example-store.test/us/app/plaxo-بلاكسو/id9072514863?ls=1
Try using the app as Guest.

Target Market(s)

Kuwait

Font styles to use
Serif
Sans Serif

Requirements
Must have
• Home Screens
The home page should have everything from the existing app and a quick area to change between different kid's profile to see activities matching their interests ONLY. In the current version, there's no switch profile and hence we are showing the name tags on the activities.

We are also going to build ecommerce so we need that ecommerce look and feel.
Kindly maintain the image aspect ratio from the current app so the new version doesn't require new images.

Need a complete new innovative designs - Keep the color scheme same.
The designs should be minimalistic and image oriented. The design should be done in XD. The designs should be submitted in both light and dark theme.
Reference to be used - http://brindle.example.uk

D.M for more info if needed.

```html
<!DOCTYPE html>
<html lang="en">
<head>
<meta charset="utf-8">
<title>Schedule – Quick Actions</title>
<link rel="stylesheet" href="https://fonts.googleapis.com/css2?family=Poppins:wght@400;500;600;700&display=swap">
<style>
  :root {
    --orange: #f9a93d;
    --ink: #111111;
    --muted: #c9c9c9;
    --nav-bg: #eefcfd;
    --nav-icon: #8a8f92;
    --screen: #ffffff;
  }
  * { box-sizing: border-box; margin: 0; padding: 0; }
  html, body { width: 1200px; height: 1200px; overflow: hidden; background: #ffffff; font-family: "Poppins", sans-serif; }
  .screen {
    position: absolute; left: 362px; top: 85px; width: 476px; height: 1030px;
    background: var(--screen); overflow: hidden;
    box-shadow: 0 4px 40px rgba(0,0,0,0.28);
  }
  .schedule { position: absolute; inset: 0; }
  .abs { position: absolute; }
  .center-x { transform: translateX(-50%); white-space: nowrap; }
  .title { left: 238px; top: 86px; font-size: 22px; font-weight: 700; color: var(--muted); letter-spacing: 0.5px; }
  .back { left: 52px; top: 66px; }
  .avatar { left: 384px; top: 55px; width: 52px; height: 52px; border-radius: 50%;
    background: radial-gradient(circle at 50% 45%, #fbe3c9, #fdf1e4); }
  .month { top: 207px; font-size: 22px; color: #f2f2f2; }
  .month.current { font-weight: 600; font-size: 24px; color: var(--muted); }
  .day { top: 311px; text-align: center; color: #ececec; width: 60px; margin-left: -30px; }
  .day .num { font-size: 22px; line-height: 26px; }
  .day .name { font-size: 15px; margin-top: 2px; }
  .day-pill { left: 199px; top: 266px; width: 79px; height: 140px; border-radius: 40px; background: #fffaf1; }
  .time { font-size: 18px; color: #e2e2e2; width: 130px; margin-left: -65px; text-align: center; }
  .card { left: 166px; width: 251px; height: 90px; border-radius: 45px; padding: 16px 0 0 35px; color: #ffffff; }
  .card .name { font-size: 18px; font-weight: 600; opacity: 0.8; }
  .card .hours { font-size: 13px; opacity: 0.8; margin-top: 2px; }
  .card.pink { top: 499px; background: #fff4f6; }
  .card.blue { top: 685px; background: #f8f9ff; }
  .card.mint { top: 797px; background: #f4fdf8; }
  .progress { left: 166px; top: 606px; }
  .status { left: 240px; top: 627px; font-size: 14px; color: #f1eeee; }
  .veil { position: absolute; inset: 0; background: rgba(255,255,255,0.55); }

  .nav { position: absolute; left: 0; bottom: 0; width: 476px; height: 86px; background: var(--nav-bg);
    border-radius: 37px 37px 0 0; }
  .nav svg { position: absolute; top: 22px; }
  .fab-well { position: absolute; left: 190px; top: 903px; width: 96px; height: 96px; border-radius: 50%;
    background: linear-gradient(180deg, rgba(216,216,216,0) 20%, #d4d4d4 60%, #c4c4c4); }
  .fab { position: absolute; border-radius: 50%; background: var(--orange); display: flex; align-items: center; justify-content: center; }
  .fab.main { left: 203px; top: 916px; width: 70px; height: 70px; box-shadow: 0 0 18px rgba(249,169,61,0.55); }
  .fab.profile { left: 190px; top: 780px; width: 96px; height: 96px; box-shadow: 0 0 26px rgba(249,169,61,0.6); }
  .fab.task { left: 93px; top: 855px; width: 62px; height: 62px; }
  .fab.online { left: 322px; top: 855px; width: 62px; height: 62px; }
  .action-label { position: absolute; font-size: 14px; color: var(--ink); white-space: nowrap; transform: translateX(-50%); }
  .action-label.strong { font-weight: 600; font-size: 15px; }
</style>
</head>
<body>
<main class="screen">
  <section class="schedule" aria-hidden="true">
    <svg class="abs back" width="24" height="30" viewBox="0 0 24 30"><path d="M17 4 L7 15 L17 26" fill="none" stroke="#e0e0e0" stroke-width="3" stroke-linecap="round" stroke-linejoin="round"/></svg>
    <div class="abs title center-x">SCHEDULE</div>
    <div class="abs avatar" role="img" aria-label="Kid profile illustration"></div>

    <div class="abs month center-x" style="left:66px">August</div>
    <div class="abs month current center-x" style="left:238px">September</div>
    <div class="abs month center-x" style="left:404px">October</div>

    <div class="abs day-pill"></div>
    <div class="abs day" style="left:17px"><div class="num">10</div><div class="name">Sun</div></div>
    <div class="abs day" style="left:127px"><div class="num">11</div><div class="name">Mon</div></div>
    <div class="abs day" style="left:238px"><div class="num">12</div><div class="name">Tue</div></div>
    <div class="abs day" style="left:346px"><div class="num">13</div><div class="name">Wed</div></div>
    <div class="abs day" style="left:456px"><div class="num">14</div><div class="name">Thu</div></div>

    <div class="abs time" style="left:86px;top:528px">10.00 AM</div>
    <div class="abs card pink"><div class="name">Puzzles</div><div class="hours">10.00 am - 12.00 pm</div></div>
    <svg class="abs progress" width="252" height="14" viewBox="0 0 252 14">
      <line x1="7" y1="7" x2="245" y2="7" stroke="#fbe9ed" stroke-width="2"/>
      <circle cx="7" cy="7" r="6" fill="#fde3e9"/><circle cx="126" cy="7" r="6" fill="#fde3e9"/><circle cx="245" cy="7" r="6" fill="#fde3e9"/>
    </svg>
    <svg class="abs" style="left:208px;top:624px" width="18" height="20" viewBox="0 0 18 20"><circle cx="11" cy="3" r="2" fill="#ececec"/><path d="M4 19 L8 11 L12 14 L13 8 M6 9 L10 7 L14 10" fill="none" stroke="#ececec" stroke-width="1.6" stroke-linecap="round"/></svg>
    <div class="abs status">Starting, 2 hours left</div>

    <div class="abs time" style="left:86px;top:714px">01.00 PM</div>
    <div class="abs card blue"><div class="name">Tye Dye</div><div class="hours">01.00 pm - 03.00 pm</div></div>

    <div class="abs time" style="left:86px;top:827px">03.00 PM</div>
    <div class="abs card mint"><div class="name">Art Club</div><div class="hours">03.00 pm - 05.00 pm</div></div>
    <div class="veil"></div>
  </section>

  <div class="action-label strong" style="left:238px;top:740px">Switch Profile</div>
  <div class="action-label" style="left:79px;top:824px">Add New Task</div>
  <div class="action-label" style="left:399px;top:824px">Online Class</div>

  <a class="fab profile" aria-label="Switch Profile">
    <svg width="70" height="70" viewBox="0 0 70 70"><circle cx="35" cy="35" r="31" fill="none" stroke="#111" stroke-width="6"/><circle cx="35" cy="27" r="9" fill="#111"/><path d="M18 52 C21 41 49 41 52 52" fill="#111"/></svg>
  </a>
  <a class="fab task" aria-label="Add New Task">
    <svg width="30" height="34" viewBox="0 0 30 34"><path d="M4 3 H19 L26 10 V31 H4 Z" fill="none" stroke="#111" stroke-width="3" stroke-linejoin="round"/><path d="M19 3 V10 H26" fill="none" stroke="#111" stroke-width="3"/><path d="M15 15 V27 M9 21 H21" stroke="#111" stroke-width="3"/></svg>
  </a>
  <a class="fab online" aria-label="Online Class">
    <svg width="34" height="24" viewBox="0 0 34 24"><rect x="1" y="3" width="21" height="18" rx="3" fill="#111"/><path d="M22 12 L33 4 V20 Z" fill="#111"/></svg>
  </a>

  <nav class="nav" aria-label="Main">
    <svg style="left:35px" width="40" height="40" viewBox="0 0 40 40"><path d="M4 20 L20 5 L36 20 M9 16 V36 H16 V25 H24 V36 H31 V16" fill="none" stroke="var(--nav-icon)" stroke-width="3.5" stroke-linejoin="round"/></svg>
    <svg style="left:120px" width="44" height="44" viewBox="0 0 44 44"><circle cx="22" cy="22" r="19" fill="none" stroke="var(--nav-icon)" stroke-width="3.5"/><path d="M30 14 L25 25 L14 30 L19 19 Z" fill="none" stroke="var(--nav-icon)" stroke-width="3" stroke-linejoin="round"/></svg>
    <svg style="left:315px" width="40" height="44" viewBox="0 0 40 44"><rect x="3" y="7" width="34" height="34" rx="3" fill="none" stroke="var(--nav-icon)" stroke-width="3.5"/><rect x="3" y="7" width="34" height="9" fill="var(--nav-icon)"/><path d="M11 2 V9 M29 2 V9" stroke="var(--nav-icon)" stroke-width="3.5"/><path d="M11 24 H14 M19 24 H22 M27 24 H30" stroke="var(--nav-icon)" stroke-width="3"/></svg>
    <svg style="left:399px" width="44" height="44" viewBox="0 0 44 44"><circle cx="22" cy="22" r="19" fill="none" stroke="var(--nav-icon)" stroke-width="3.5"/><circle cx="22" cy="17" r="6" fill="none" stroke="var(--nav-icon)" stroke-width="3.5"/><path d="M10 34 C14 26 30 26 34 34" fill="none" stroke="var(--nav-icon)" stroke-width="3.5"/></svg>
  </nav>
  <div class="fab-well"></div>
  <a class="fab main" aria-label="Close quick actions">
    <svg width="30" height="30" viewBox="0 0 30 30"><path d="M15 2 V28 M2 15 H28" stroke="#fff" stroke-width="6"/></svg>
  </a>
</main>
</body>
</html>
```